New labels for new line of supplements

I'm starting a new line of supplements and I need a label created for the first supplement - Blood Sugar Support.
The supplement line is by Corvane Nutrition. What I'm really looking for is label that can be used again for the next supplement and consumers would recognize the label layout as a Corvane Nutrition product. I've attached an example from Meltiq Nutrition to have a look at. I've also attached my "Corvane Skin Care" logo that needs to be turned into Corvane Nutrition. Just change Skin Care to Nutrition.
Target Market(s)
Shopvexa consumers
Font styles to use
Colors
Designer to choose colors to be used in the design.
Requirements
Must have
- Instantly recognizable as my brand

```html
<!DOCTYPE html>
<html lang="en">
<head>
<meta charset="UTF-8">
<title>Corvane Nutrition – Blood Sugar Support Label</title>
<link href="https://fonts.googleapis.com/css2?family=Lato:wght@400;700;900&display=swap" rel="stylesheet">
<style>
  :root {
    --brand-red: #d12a36;
    --brand-red-deep: #b81f2b;
    --label-white: #ffffff;
    --tag-cream: #f1e8d2;
    --ink-dark: #2a1a14;
    --page-bg: #eceae6;
    --caption-ink: #b81f2b;
  }
  * { box-sizing: border-box; margin: 0; padding: 0; }
  html, body {
    width: 1200px; height: 900px; overflow: hidden;
    background: var(--page-bg);
    font-family: "Lato", Arial, sans-serif;
  }
  .label {
    position: absolute; left: 190px; top: 20px;
    width: 820px; height: 860px;
    background: var(--label-white);
    overflow: hidden;
  }
  .label__red-field { position: absolute; left: 0; top: 0; width: 820px; height: 580px; }
  .brand {
    position: absolute; top: 56px; left: 0; width: 100%;
    text-align: center; color: var(--label-white);
    font-weight: 700; font-size: 30px; letter-spacing: 6px;
  }
  .title {
    position: absolute; top: 130px; left: 0; width: 100%;
    text-align: center; color: var(--label-white);
    font-weight: 900; font-size: 118px; line-height: 1.0; letter-spacing: 2px;
  }
  .title__tag {
    position: absolute; top: 390px; left: 50%; transform: translateX(-50%);
    background: var(--tag-cream); color: var(--ink-dark);
    font-weight: 900; font-size: 92px; line-height: 1; padding: 6px 26px 12px;
    letter-spacing: 2px; white-space: nowrap;
  }
  .benefits {
    position: absolute; top: 590px; left: 40px; width: 740px;
    display: flex; justify-content: space-between;
  }
  .benefit { width: 240px; text-align: center; }
  .benefit__icon { height: 110px; display: flex; align-items: center; justify-content: center; }
  .benefit__text {
    margin-top: 12px; color: var(--caption-ink);
    font-weight: 900; font-size: 21px; line-height: 1.2; text-transform: uppercase;
    white-space: nowrap;
  }
  .icon-placeholder {
    width: 110px; height: 100px; border-radius: 50%;
    background: radial-gradient(circle at 50% 40%, #e0474f, var(--brand-red-deep));
  }
  .pack-info {
    position: absolute; right: 70px; top: 762px; text-align: right;
    color: var(--caption-ink); line-height: 1.1;
  }
  .pack-info__kind { font-size: 14px; font-weight: 700; }
  .pack-info__count { font-size: 22px; font-weight: 900; }
  .label__band { position: absolute; left: 0; top: 808px; width: 100%; height: 14px; background: var(--brand-red); }
  .label__rule { position: absolute; left: 0; top: 836px; width: 100%; height: 6px; background: var(--brand-red); }
</style>
</head>
<body>
  <main class="label">
    <svg class="label__red-field" viewBox="0 0 820 580" aria-hidden="true">
      <path d="M0 0 H820 V430 C640 400 520 470 360 520 C220 560 100 560 0 540 Z" fill="var(--brand-red)"/>
      <rect x="0" y="0" width="820" height="8" fill="var(--brand-red-deep)"/>
    </svg>

    <div class="brand">CORVANE NUTRITION</div>

    <h1 class="title">BLOOD<br>SUGAR</h1>
    <div class="title__tag">SUPPORT</div>

    <section class="benefits">
      <div class="benefit">
        <div class="benefit__icon">
          <svg width="80" height="104" viewBox="0 0 80 104" aria-hidden="true">
            <path d="M40 2 C40 2 4 50 4 68 A36 36 0 0 0 76 68 C76 50 40 2 40 2 Z" fill="var(--brand-red)"/>
            <rect x="34" y="50" width="12" height="36" fill="#fff"/>
            <rect x="22" y="62" width="36" height="12" fill="#fff"/>
          </svg>
        </div>
        <p class="benefit__text">Supports healthy<br>blood sugar</p>
      </div>
      <div class="benefit">
        <div class="benefit__icon">
          <div class="icon-placeholder" role="img" aria-label="Icon of a virus held above an open hand"></div>
        </div>
        <p class="benefit__text">Immune<br>function support</p>
      </div>
      <div class="benefit">
        <div class="benefit__icon">
          <svg width="96" height="100" viewBox="0 0 96 100" aria-hidden="true">
            <path d="M16 6 h16 v16 h16 v16 h-16 v16 h-16 v-16 h-16 v-16 h16 z" fill="var(--brand-red)"/>
            <path d="M56 30 h12 v12 h12 v12 h-12 v12 h-12 v-12 h-12 v-12 h12 z" fill="var(--brand-red)"/>
            <path d="M30 62 h10 v10 h10 v10 h-10 v10 h-10 v-10 h-10 v-10 h10 z" fill="var(--brand-red)"/>
          </svg>
        </div>
        <p class="benefit__text">Plus much more !</p>
      </div>
    </section>

    <div class="pack-info">
      <div class="pack-info__kind">Dietary Supplement</div>
      <div class="pack-info__count">60 Capsules</div>
    </div>

    <div class="label__band"></div>
    <div class="label__rule"></div>
  </main>
</body>
</html>
```